THE BRISK HOLLOW BEER

I want a beerlabel for this project.
It has to be enjoyable to look at. Some funny images and maybe some quotes on it.
This beer is about friends grabbing a pint in a pub.
Colors free to use except shiny colors I don't like.
The alcohol content is 5,7 % ABV 330ML
Target Market(s)
Young people 22 to 30 years old
Font styles to use
Serif
Decorative
Script
Colors
ffffff
000000
feeeee
Requirements
Must have
- coolness, some trendy design.
- Make sure it is a label and not a total bottle wrap.
Nice to have
- it has to feel good to drink.
Should not have
- shiny colors

```html
<!DOCTYPE html>
<html lang="en">
<head>
<meta charset="utf-8">
<title>The Brisk Hollow Beer – Label Set</title>
<link rel="stylesheet" href="https://fonts.googleapis.com/css2?family=Stint+Ultra+Condensed&family=Oswald:wght@400;500&display=swap">
<style>
  :root {
    --canvas-bg: #ececec;
    --label-black: #141414;
    --label-dark: #262626;
    --label-rim: #9c9c9c;
    --label-rim-dark: #5a5a5a;
    --title-white: #ffffff;
    --banner-red: #c4281f;
    --banner-text: #f6b73c;
    --bubble-brown: #3b2412;
    --bubble-orange: #f0922b;
    --crest-grey: #8d8d8d;
    --meta-grey: #cfcfcf;
  }
  * { margin: 0; padding: 0; box-sizing: border-box; }
  html, body { width: 903px; height: 1200px; overflow: hidden; }
  body { background: var(--canvas-bg); position: relative; }

  .label { position: absolute; }
  .label svg.label-shape { position: absolute; inset: 0; width: 100%; height: 100%; }
  .label .text { position: absolute; left: 0; width: 100%; text-align: center; }

  .title-line {
    font-family: "Stint Ultra Condensed", serif;
    color: var(--title-white);
    line-height: 1;
    text-shadow: 0 3px 0 #000, 0 0 6px rgba(0,0,0,.8);
    white-space: nowrap;
  }

  /* neck label */
  .neck-label { left: 291px; top: 40px; width: 320px; height: 240px; }
  .neck-label .brand-name { top: 74px; font-size: 46px; }
  .neck-label .brand-kind { top: 108px; font-size: 40px; }
  .neck-label .vintage { top: 165px; font-size: 11px; }

  /* main label */
  .main-label { left: 171px; top: 330px; width: 560px; height: 740px; }
  .main-label .hero-banner {
    top: 96px;
    font-family: "Oswald", sans-serif;
    font-weight: 500;
    font-size: 27px;
    line-height: 1.05;
    color: var(--banner-text);
    letter-spacing: .5px;
  }
  .main-label .hero-quote {
    top: 404px;
    font-family: "Oswald", sans-serif;
    font-size: 13px;
    line-height: 1.3;
    color: var(--bubble-orange);
  }
  .main-label .brand-name { top: 455px; font-size: 90px; }
  .main-label .brand-kind { top: 520px; font-size: 82px; }
  .main-label .vintage { top: 624px; font-size: 20px; }

  .vintage {
    font-family: "Stint Ultra Condensed", serif;
    color: var(--title-white);
    font-weight: 400;
  }
  .abv-text {
    font-family: "Stint Ultra Condensed", serif;
    fill: var(--meta-grey);
  }
</style>
</head>
<body>

<!-- Neck label -->
<section class="label neck-label" aria-label="Neck label">
  <svg class="label-shape" viewBox="0 0 320 240">
    <defs>
      <radialGradient id="neckBody" cx="50%" cy="45%" r="60%">
        <stop offset="0" stop-color="#3a3a3a"/>
        <stop offset="1" stop-color="#121212"/>
      </radialGradient>
      <linearGradient id="neckCrest" x1="0" y1="0" x2="0" y2="1">
        <stop offset="0" stop-color="#a8a8a8"/>
        <stop offset="1" stop-color="#5c5c5c"/>
      </linearGradient>
      <path id="neckArc" d="M92,196 Q160,228 228,196"/>
    </defs>
    <rect class="crest" x="108" y="2" width="104" height="48" rx="22" fill="url(#neckCrest)" role="img" aria-label="Ornamental crest with paw print"/>
    <path class="body" d="M44,150 L44,90 C44,60 90,46 160,46 C230,46 276,60 276,90 L276,150 L276,165 C276,212 222,234 160,234 C98,234 44,212 44,165 Z"
          fill="url(#neckBody)" stroke="var(--label-rim)" stroke-width="3"/>
    <path class="band" d="M4,66 L316,66 L316,148 L4,148 Z" fill="var(--label-black)" stroke="var(--label-rim-dark)" stroke-width="3"/>
    <line x1="10" y1="72" x2="310" y2="72" stroke="#444" stroke-width="1"/>
    <circle cx="160" cy="172" r="15" fill="#222" stroke="var(--meta-grey)" stroke-width="1.5"/>
    <text class="abv-text" font-size="13" text-anchor="middle">
      <textPath href="#neckArc" startOffset="50%">5,7 % ABV  |  330ML</textPath>
    </text>
  </svg>
  <div class="text title-line brand-name">THE BRISK HOLLOW</div>
  <div class="text title-line brand-kind">BEER</div>
  <div class="text vintage">2018</div>
</section>

<!-- Main label -->
<section class="label main-label" aria-label="Main label">
  <svg class="label-shape" viewBox="0 0 560 740">
    <defs>
      <radialGradient id="mainBody" cx="50%" cy="40%" r="65%">
        <stop offset="0" stop-color="#3e3e3e"/>
        <stop offset=".6" stop-color="#1e1e1e"/>
        <stop offset="1" stop-color="#0e0e0e"/>
      </radialGradient>
      <linearGradient id="mainCrest" x1="0" y1="0" x2="0" y2="1">
        <stop offset="0" stop-color="#b0b0b0"/>
        <stop offset="1" stop-color="#585858"/>
      </linearGradient>
      <radialGradient id="mascotArea" cx="45%" cy="50%" r="60%">
        <stop offset="0" stop-color="#bdbdbd"/>
        <stop offset=".55" stop-color="#6d6d6d"/>
        <stop offset="1" stop-color="#2b2b2b"/>
      </radialGradient>
      <path id="mainArc" d="M150,672 Q280,730 410,672"/>
    </defs>

    <rect class="crest" x="190" y="2" width="180" height="84" rx="38" fill="url(#mainCrest)" role="img" aria-label="Ornamental crest with paw print"/>

    <path class="body" d="M52,460 L52,250 C52,130 160,68 280,68 C400,68 508,130 508,250 L508,460 L508,585 C508,685 410,730 280,730 C150,730 52,685 52,585 Z"
          fill="url(#mainBody)" stroke="var(--label-rim)" stroke-width="5"/>
    <path d="M66,460 L66,252 C66,142 170,84 280,84 C390,84 494,142 494,252 L494,585 C494,675 404,716 280,716 C156,716 66,675 66,585 Z"
          fill="none" stroke="#333" stroke-width="2"/>

    <rect class="mascot" x="150" y="170" width="270" height="230" rx="40" fill="url(#mascotArea)" role="img" aria-label="Cartoon monkey raising a foaming glass of beer"/>

    <rect class="hero-banner-shape" x="160" y="88" width="240" height="76" fill="var(--banner-red)" stroke="#7a7a7a" stroke-width="3"/>

    <rect class="quote-bubble" x="186" y="396" width="188" height="48" rx="16" fill="var(--bubble-brown)" stroke="var(--bubble-orange)" stroke-width="1.5"/>
    <path d="M352,396 L362,384 L360,398 Z" fill="var(--bubble-brown)" stroke="var(--bubble-orange)" stroke-width="1.5"/>

    <path class="band" d="M4,452 L556,452 L556,566 L4,566 Z" fill="var(--label-black)" stroke="var(--label-rim-dark)" stroke-width="4"/>
    <line x1="14" y1="460" x2="546" y2="460" stroke="#444" stroke-width="1.5"/>
    <line x1="14" y1="558" x2="546" y2="558" stroke="#444" stroke-width="1.5"/>

    <path d="M120,608 Q280,660 440,608" fill="none" stroke="#777" stroke-width="1.5" stroke-dasharray="5 4"/>
    <circle cx="280" cy="637" r="26" fill="#222" stroke="var(--meta-grey)" stroke-width="2"/>

    <text class="abv-text" font-size="22" text-anchor="middle">
      <textPath href="#mainArc" startOffset="50%">5,7 % ABV  |  330ML</textPath>
    </text>
  </svg>

  <div class="text hero-banner">TODAY<br>I WAS A HERO</div>
  <div class="text hero-quote">I rescued some beer that was<br>trapped in a bottle.</div>
  <div class="text title-line brand-name">THE BRISK HOLLOW</div>
  <div class="text title-line brand-kind">BEER</div>
  <div class="text vintage">2018</div>
</section>

</body>
</html>
```